Brill Insurance Agency - Business Cards

Hello, I am needing new trendy business cards for our Insurance Agency now that I have a new Logo. I have attached our new logo with several color options along with a business card design that I like. I am leaning towards burgundy and blue colors. I have attached our current business card. I have also attached a headshot of our company president, Martin Vale, that you can use if you wish. Thank you so much in advance for all the wonderful designs!!!!

Target Market(s)

We want to look very professional to potential customers and we also want to look very professional so insurance companies will want to contract with us to sell their product.

Industry/Entity Type

Insurance

Contact Information for Business Card

Martin Vale
mvale@brillagency.com
Business: 555-213-4087
Fax: 555-213-7751
Cell: 555-390-2618
Toll Free: 888-555-0194
42 W Elm Rd Butler, MO 64730
www.brillagency.net

Font styles to use
Serif
Sans Serif

Colors
0355a3
3277b5
f04a50
ec1f27

Requirements
Nice to have
• I love creativity. The more creative and balanced a business card design the more I will like it. I would like the card to be printed horizontally instead of vertically.
Should not have
• My project should not have the Allied Coverage Network logo. It is no longer used in the industry.

```html
<!DOCTYPE html>
<html lang="en">
<head>
<meta charset="utf-8">
<title>Brill Insurance Agency – Business Cards</title>
<link rel="stylesheet" href="https://fonts.googleapis.com/css2?family=Jost:wght@400;600&display=swap">
<style>
  :root {
    --backdrop: #2b2d2c;
    --burgundy: #561129;
    --charcoal: #4d4d4d;
    --logo-grey: #4f4f52;
    --white: #ffffff;
    --ink: #3a3a3a;
  }
  * { box-sizing: border-box; margin: 0; padding: 0; }
  html, body { width: 1082px; height: 1200px; overflow: hidden; }
  body {
    position: relative;
    background: var(--backdrop);
    font-family: "Jost", "Helvetica Neue", Arial, sans-serif;
  }
  .card {
    position: absolute;
    left: 240px;
    width: 659px;
    height: 366px;
    border-radius: 22px;
    overflow: hidden;
  }
  .card--front { top: 208px; background: var(--burgundy); }
  .card--back { top: 626px; background: var(--white); }

  .brand {
    position: absolute;
    display: flex;
    align-items: center;
  }
  .brand__dot {
    border-radius: 50%;
    border: 5px solid currentColor;
    flex: none;
  }
  .brand__rule { width: 2px; background: currentColor; flex: none; }
  .brand__name {
    font-weight: 600;
    line-height: 1.05;
    text-transform: uppercase;
    white-space: nowrap;
  }
  .brand__name span { display: block; letter-spacing: 0.32em; text-align: center; }

  .card--front .brand { left: 138px; top: 176px; color: var(--logo-grey); }
  .card--front .brand__dot { width: 80px; height: 80px; }
  .card--front .brand__rule { height: 92px; margin: 0 14px; }
  .card--front .brand__name { font-size: 30px; }
  .card--front .brand__name span { font-size: 16px; }

  .card--back .brand { left: 34px; top: 24px; color: var(--logo-grey); }
  .card--back .brand__dot { width: 78px; height: 78px; }
  .card--back .brand__rule { height: 92px; margin: 0 14px; }
  .card--back .brand__name { font-size: 29px; color: var(--burgundy); }
  .card--back .brand__name span { font-size: 16px; }

  .person {
    position: absolute;
    right: 243px;
    top: 116px;
    text-align: right;
    line-height: 1.1;
  }
  .person__name { font-size: 30px; color: var(--burgundy); font-weight: 400; }
  .person__title { font-size: 20px; color: var(--ink); }

  .contact-panel {
    position: absolute;
    left: 0; top: 177px;
    width: 442px; height: 189px;
    background: var(--charcoal);
    color: var(--white);
    padding: 18px 0 0 32px;
    font-size: 19px;
    line-height: 25px;
  }
  .contact-panel__address { position: absolute; left: 32px; top: 136px; white-space: nowrap; }

  .side-panel {
    position: absolute;
    left: 448px; top: 0;
    width: 211px; height: 366px;
    background: var(--burgundy);
    color: var(--white);
  }
  .headshot {
    position: absolute;
    left: 38px; top: 26px;
    width: 146px; height: 181px;
    border: 2px solid var(--white);
    background: linear-gradient(180deg, #6d6f6e 0%, #8a7d74 55%, #1d1f24 100%);
  }
  .web {
    position: absolute;
    right: 24px; top: 292px;
    text-align: right;
    font-size: 16.5px;
    line-height: 26px;
    white-space: nowrap;
  }
</style>
</head>
<body>
  <section class="card card--front">
    <div class="brand">
      <div class="brand__dot"></div>
      <div class="brand__rule"></div>
      <div class="brand__name">Brill Insurance<span>Agency Inc</span></div>
    </div>
  </section>

  <section class="card card--back">
    <div class="brand">
      <div class="brand__dot"></div>
      <div class="brand__rule"></div>
      <div class="brand__name">Brill Insurance<span>Agency Inc</span></div>
    </div>

    <div class="person">
      <p class="person__name">Martin Vale</p>
      <p class="person__title">CEO</p>
    </div>

    <div class="contact-panel">
      <p>Office: 555 213 4087 ext. 23</p>
      <p>Fax: 555 213 7751</p>
      <p>Cell: 555 390 2618</p>
      <p>Toll Free: 888 555 0194</p>
      <p class="contact-panel__address">42 W Elm Rd P.O. Box 218 Marlow, OR 97021</p>
    </div>

    <div class="side-panel">
      <div class="headshot" role="img" aria-label="Headshot of Martin Vale"></div>
      <div class="web">
        <p>mvale@brillagency.com</p>
        <p>www.brillagency.net</p>
      </div>
    </div>
  </section>
</body>
</html>
```